Real Estate Entrepreneur needs a business card

I am a real estate entrepreneur, I buy houses for investment purposes, I act as a real estate agent representing buyers and sellers in residential home transactions, I am a contractor that does a wide range of home repairs and construction. I'd like a design that can stick with me through the years as my business grows and morphs to fit any niche I decide to pursue as markets change.

Target Market(s)

Anyone with interest that may be related to real estate.

Industry/Entity Type

Real Estate

Contact Information for Business Card

A card that stands out and doesn't put me in any one box. My business will evolve over time and I need a card that can stay relevant.

Colors

Designer to choose colors to be used in the design.

Requirements
Must have
• Character
Nice to have
• I'm open
Should not have
• Cliche houses and hammers

```html
<!DOCTYPE html>
<html lang="en">
<head>
<meta charset="utf-8">
<title>Reid Calloway – Business Card</title>
<link href="https://fonts.googleapis.com/css2?family=Montserrat:wght@500;800&family=Roboto:wght@400&display=swap" rel="stylesheet">
<style>
  :root {
    --backdrop: #2b2b2d;
    --paper: #ecebe8;
    --ink: #262626;
    --ink-soft: #3a3a3a;
    --night: #1d1d1f;
    --gold: #c9b27a;
    --gold-light: #e2d2a2;
    --white: #f4f4f4;
  }
  * { margin: 0; padding: 0; box-sizing: border-box; }
  html, body {
    width: 1200px; height: 900px; overflow: hidden;
    background: var(--backdrop);
  }
  .canvas {
    position: relative; width: 1200px; height: 900px;
    display: flex; justify-content: center; align-items: center; gap: 60px;
  }
  .card {
    width: 420px; height: 700px; border-radius: 38px;
    display: flex; flex-direction: column; align-items: center;
    padding-top: 150px;
  }
  .card--front { background: var(--paper); color: var(--ink); }
  .card--back { background: var(--night); color: var(--white); }

  .brand-dot {
    width: 120px; height: 120px; border-radius: 50%;
    background: radial-gradient(circle at 35% 30%, var(--gold-light), var(--gold) 70%);
    margin-bottom: 40px;
  }
  .brand-name {
    font-family: "Montserrat", sans-serif; font-weight: 800;
    font-size: 40px; letter-spacing: 1px; line-height: 1;
    text-transform: uppercase;
  }
  .brand-role {
    font-family: "Montserrat", sans-serif; font-weight: 500;
    font-size: 21px; letter-spacing: 1px; margin-top: 8px;
  }
  .rule {
    width: 18px; height: 3px; background: var(--ink); margin: 30px 0 26px;
  }
  .rule--end { margin: 22px 0 0; }
  .icons { display: flex; gap: 22px; margin-bottom: 28px; }
  .icon {
    width: 26px; height: 26px; border-radius: 50%; background: var(--ink);
    display: flex; align-items: center; justify-content: center;
  }
  .icon svg { width: 14px; height: 14px; }
  .contact {
    list-style: none; text-align: center;
    font-family: "Roboto", sans-serif; font-size: 20px; color: var(--ink-soft);
    line-height: 1; 
  }
  .contact li + li { margin-top: 22px; }
  .card--back .brand-dot { margin-top: 60px; }
</style>
</head>
<body>
<main class="canvas">
  <section class="card card--front">
    <div class="brand-dot" aria-hidden="true"></div>
    <h1 class="brand-name">Reid Calloway</h1>
    <p class="brand-role">Real Estate Agent</p>
    <div class="rule"></div>
    <div class="icons">
      <span class="icon" aria-label="phone">
        <svg viewBox="0 0 16 16"><path d="M4 1.5l2.2 3-1.3 1.4a8 8 0 0 0 5.2 5.2l1.4-1.3 3 2.2-1.2 2.4C7.6 14.4 1.6 8.4 1.6 2.7z" fill="#fff"/></svg>
      </span>
      <span class="icon" aria-label="email">
        <svg viewBox="0 0 16 16"><rect x="2" y="4" width="12" height="8" fill="#fff"/><path d="M2 4l6 5 6-5" fill="none" stroke="#262626" stroke-width="1.2"/></svg>
      </span>
      <span class="icon" aria-label="website">
        <svg viewBox="0 0 16 16"><g fill="none" stroke="#fff" stroke-width="1.6"><rect x="5" y="1.5" width="5" height="7" rx="2.5" transform="rotate(30 7.5 5)"/><rect x="6" y="7.5" width="5" height="7" rx="2.5" transform="rotate(30 8.5 11)"/></g></svg>
      </span>
    </div>
    <ul class="contact">
      <li>042-555-0147</li>
      <li>hello@reidcalloway.com</li>
      <li>www.reidcalloway.com</li>
    </ul>
    <div class="rule rule--end"></div>
  </section>

  <section class="card card--back">
    <div class="brand-dot" aria-hidden="true"></div>
    <h2 class="brand-name">Reid Calloway</h2>
    <p class="brand-role">Real Estate Agent</p>
  </section>
</main>
</body>
</html>
```